WordPress Classical Pianist Website, one pager with one one-pager as a subsite

Hi everyone,

I'm looking for a long-term freelance designer to refresh and modernize my existing WordPress website (www.velharo.com).
The new layout should be a clean one-page design with one one-pager subpage (CD's subpage).

From time to time, I also need help with smaller design projects such as concert flyers, CD covers (including booklets), and other promotional materials — that’s why I’m looking for a long-term collaboration.

The website is fully functional; I just need a fresh visual update that matches the style of my new CD and future materials.

Experience with WordPress is essential.
I'm looking for someone reliable, creative, and easy to communicate with — not a large agency.

Thanks a lot!
Tobias

Target Market(s)

Classical music audience, concert organizers (!), music students/music universities and piano music lovers worldwide.

Industry/Entity Type

Classical Music / Artist Portfolio

Coding

Coded - Design and coding required

Number of Pages Required

2 page

Other font styles liked:
• Ephesis Bold, Lexend Tera, Lexend Tera Medium, Adobe Fnt23

Requirements
Must have
• Clean and elegant one-page layout with 1–2 subpages (Bio, Concerts, Contact); high-quality visual design reflecting a professional concert pianist’s identity; visual harmony with my new CD “Sotto la Bruma” (colors, mood, tone); integration of photos, videos, CD covers, and short audio samples via a mini audio player; all existing content to be transferred from www.velharo.com ; bilingual structure (German/English); responsive design (desktop + mobile); built on WordPress
Nice to have
• Subtle animations or transitions between sections (smooth scrolling or fade-ins), elegant typography inspired by classical music aesthetics (fonts below), optional dark / light mode design, small music/video player or integrated streaming links (Tunevale, Cedar Sound, ClipHarbor)
Should not have
• Overloaded or cluttered layout, flashy or bright color schemes, stock photos unrelated to piano or classical music, heavy animations or slow loading times, generic, template-looking WordPress themes

```html
<!DOCTYPE html>
<html lang="en">
<head>
<meta charset="utf-8">
<title>Tobias Velharo — Pianist</title>
<link href="https://fonts.googleapis.com/css2?family=Lato:wght@300;400&family=Poppins:wght@300;400;500;600&display=swap" rel="stylesheet">
<style>
:root{
  --black:#050505;
  --teal:#86c8d6;
  --teal-light:#b9dfe7;
  --teal-deep:#1f8fa6;
  --slate:#6e9298;
  --white:#ffffff;
  --ink:#222;
  --muted:#666;
  --dot:#4fb3c9;
}
*{margin:0;padding:0;box-sizing:border-box}
html,body{width:1200px;height:4494px;overflow:hidden}
body{position:relative;font-family:'Poppins',sans-serif;color:var(--ink);background:var(--white)}
.abs{position:absolute}
.hero{left:0;top:0;width:1200px;height:580px;background:var(--black)}
.brand{font-family:'Poppins',sans-serif;font-weight:500;color:var(--white);letter-spacing:3px}
.brand small{display:block;font-size:9px;letter-spacing:1px;font-weight:500}
.nav{top:34px;left:550px;width:490px;display:flex;justify-content:space-between;font-size:11px;color:var(--white);letter-spacing:.5px}
.hero-title{left:158px;top:218px;color:var(--white);font-family:'Lato',sans-serif;font-weight:300;line-height:1}
.hero-title .first{font-size:62px;letter-spacing:2px}
.hero-title .last{font-size:92px;letter-spacing:3px;margin-top:6px}
.social-tab{left:1165px;top:206px;width:35px;height:169px;background:var(--teal-deep);border-radius:18px 0 0 18px;display:flex;flex-direction:column;align-items:center;justify-content:center;gap:14px}
.social-tab span{width:12px;height:12px;border-radius:50%;background:var(--white)}
.keys{left:0;top:580px;width:1200px;height:52px;background:linear-gradient(#1a1a1a,#0c6f82 40%,#c9e8ef 50%,#0c6f82 60%,#1a1a1a)}
.section-h{font-family:'Lato',sans-serif;font-weight:300;font-size:32px;letter-spacing:1px;color:#222;text-align:center;width:1200px;left:0}
.bio-text{left:664px;top:753px;width:372px;font-size:11.3px;line-height:18px;color:#1e2a2c}
.btn{background:var(--black);color:var(--white);font-size:11px;font-weight:500;display:flex;align-items:center;justify-content:center}
.card{background:var(--white);width:422px;height:182px;box-shadow:0 8px 22px rgba(0,0,0,.12);padding:30px 36px}
.card h3{font-weight:500;font-size:19px;color:#2b2b2b;margin-bottom:16px}
.card li{list-style:none;font-size:12.5px;color:#555;line-height:30px;padding-left:16px;position:relative}
.card li::before{content:"";position:absolute;left:0;top:13px;width:6px;height:6px;border-radius:50%;background:var(--dot)}
.card.plain li::before{display:none}
.cover{width:278px;height:276px;position:relative}
.press-item{width:278px}
.press-item h4{font-size:15.5px;font-weight:600;line-height:20px;color:#333;margin-top:26px;width:235px}
.press-item p{font-size:11.5px;line-height:16.5px;color:#666;margin-top:6px;width:260px}
.press-item a{display:inline-block;margin-top:18px;font-size:11.5px;color:#555;text-decoration:underline}
.badge{position:absolute;top:8px;right:8px;width:58px;height:26px;background:#f0b400}
.video{width:204px;height:115px}
.foot-nav{top:4334px;left:0;width:1200px;font-size:13.5px;color:var(--white)}
.foot-nav span{position:absolute;transform:translateX(-50%)}
.contact{top:4398px;font-size:12.5px;color:var(--white);display:flex;align-items:center;gap:12px}
.ico{width:26px;height:26px;border-radius:50%;background:var(--dot);display:flex;align-items:center;justify-content:center}
.dotsoc{width:14px;height:14px;border:2px solid var(--white);border-radius:50%}
</style>
</head>
<body>

<section class="hero abs">
  <div class="brand abs" style="left:160px;top:20px;font-size:22px"><small>Tobias</small>VELHARO</div>
  <nav class="nav abs"><span>HOME</span><span>BIOGRAPHY</span><span>REPERTOIRE</span><span>PRESS</span><span>MEDIA</span><span>CONTACT</span></nav>
  <div class="abs" role="img" aria-label="Black and white portrait of the pianist" style="left:640px;top:52px;width:420px;height:528px;background:radial-gradient(ellipse at 55% 45%,#9a9a9a,#3a3a3a 50%,#050505 75%)"></div>
  <div class="hero-title abs"><div class="first">TOBIAS</div><div class="last">VELHARO</div></div>
  <div class="social-tab abs"><span></span><span></span></div>
</section>
<div class="keys abs" role="img" aria-label="Piano keyboard band"></div>

<svg class="abs" style="left:0;top:632px" width="1200" height="1700" viewBox="0 632 1200 1700">
  <rect x="0" y="632" width="1200" height="1700" fill="#b9dfe7"/>
  <polygon points="0,632 1200,632 1200,1177 863,1325 0,1172" fill="#86c8d6"/>
  <polyline points="0,1172 863,1325 1200,1177" fill="none" stroke="#050505" stroke-width="7"/>
  <polygon points="0,2154 863,2302 1200,2197 1200,2332 0,2332" fill="#fff"/>
  <polyline points="0,2154 863,2302 1200,2197" fill="none" stroke="#050505" stroke-width="7"/>
</svg>

<div class="abs" style="left:203px;top:743px;width:420px;height:378px;background:var(--slate)"></div>
<div class="abs" role="img" aria-label="Portrait of the pianist in a dark suit" style="left:160px;top:706px;width:441px;height:393px;background:linear-gradient(120deg,#c9a98a,#6a5446 45%,#1d1d24 70%,#d6c2ac)"></div>
<h2 class="abs" style="left:664px;top:700px;font-family:'Lato',sans-serif;font-weight:300;font-size:32px;color:#1e2a2c">BIOGRAPHY</h2>
<p class="bio-text abs"><b>Tobias Velharo</b>, a pianist of international renown, first came to worldwide attention when he won first prize at the prestigious International Keyboard Prize in Harwick in 1994. This victory, coupled with the prize for best Romantic interpretation, opened the doors for him to major concert stages in Great Britain, Germany, Italy, Japan and the USA. As a soloist he has performed with renowned orchestras such as the Northbridge Symphony Orchestra, the Aldren Philharmonia, the Coastal Chamber Orchestra, the Orchestre de la Vallée, the Halden Philharmonic, the Southwind Philharmonia and the Meridian Symphony Orchestra. He has also worked with outstanding chamber music partners such as the Lindqvist Quartet, the Arden Quartet, Mira Ostend, Lena Corvin, Jonas Weld and Paul Brenner. These diverse experiences have deepened his understanding of interacting and playing with other musicians and given him a broader artistic perspective.</p>
<div class="btn abs" style="left:664px;top:1086px;width:126px;height:35px">Learn More</div>

<h2 class="section-h abs" style="top:1396px">REPERTOIRE</h2>
<div class="card abs" style="left:169px;top:1489px"><h3>WA Morvelli (1756 – 1791)</h3><ul><li>Piano Concerto No. 20 in D minor, K. 466</li><li>Piano Concerto No. 21 in C major, K. 467</li><li>Piano Concerto No. 23 in A major, K. 488</li></ul></div>
<div class="card plain abs" style="left:609px;top:1489px"><h3>Louis V. Brandhoff (1770 – 1827)</h3><ul><li>Piano Concerto No. 1 in C major, op. 15</li><li>Piano Concerto No. 2 in B-flat major, Op. 19</li><li>Piano Concerto No. 3 in C minor, op. 37</li></ul></div>
<div class="card abs" style="left:169px;top:1686px"><h3>Frederic Calvany (1810 – 1849)</h3><ul><li>Piano Concerto No. 20 in D minor, K. 466</li><li>Piano Concerto No. 21 in C major, K. 467</li><li>Piano Concerto No. 23 in A major, K. 488</li></ul></div>
<div class="card abs" style="left:609px;top:1686px"><h3>Franz Lisander (1811 – 1886)</h3><ul><li>Piano Concerto No. 1 in C major, op. 15</li><li>Piano Concerto No. 2 in B-flat major, Op. 19</li><li>Piano Concerto No. 3 in C minor, op. 37</li></ul></div>
<div class="card abs" style="left:169px;top:1883px"><h3>Frederic Calvany (1810 – 1849)</h3><ul><li>Piano Concerto No. 20 in D minor, K. 466</li><li>Piano Concerto No. 21 in C major, K. 467</li><li>Piano Concerto No. 23 in A major, K. 488</li></ul></div>
<div class="card abs" style="left:609px;top:1883px"><h3>Franz Lisander (1811 – 1886)</h3><ul><li>Piano Concerto No. 1 in C major, op. 15</li><li>Piano Concerto No. 2 in B-flat major, Op. 19</li><li>Piano Concerto No. 3 in C minor, op. 37</li></ul></div>
<div class="btn abs" style="left:520px;top:2112px;width:160px;height:33px">View All Repertoire</div>

<h2 class="section-h abs" style="top:2356px">PRESS</h2>
<div class="press-item abs" style="left:160px;top:2433px"><div class="cover" role="img" aria-label="CD cover: pianist in black suit on light grey, piano sonatas" style="background:linear-gradient(90deg,#2a2a2a 0,#bdbdbd 45%,#ececec)"></div><h4>Sonatas Pathetique, Aurora, Appassionata</h4><p>Appassionata" means "passionate," and Velharo stuck to that. He relied entirely on expression. He shaped the first movement with utmost expressiveness and intensity.</p><a>Learn More →</a></div>
<div class="press-item abs" style="left:460px;top:2433px"><div class="cover" role="img" aria-label="CD cover: Russian piano music, pianist at the keyboard" style="background:linear-gradient(90deg,#3a2a3c,#b38a8e 55%,#5a3a4e)"><span class="badge"></span></div><h4>Skarovin, Ravenkov, Prolanov</h4><p>Appassionata" means "passionate," and Velharo stuck to that. He relied entirely on expression. He shaped the first movement with utmost expressiveness and intensity.</p><a>Learn More →</a></div>
<div class="press-item abs" style="left:760px;top:2433px"><div class="cover" role="img" aria-label="CD cover: mazurkas, pianist on dark background" style="background:linear-gradient(90deg,#111,#555 60%,#2a2a2a)"><span class="badge"></span></div><h4>Frederic Calvany Edition Vol. 10 – Mazurkas</h4><p>Appassionata" means "passionate," and Velharo stuck to that. He relied entirely on expression. He shaped the first movement with utmost expressiveness and intensity.</p><a>Learn More →</a></div>
<div class="press-item abs" style="left:160px;top:2902px"><div class="cover" role="img" aria-label="CD cover: edition vol. 9, pianist in black" style="background:linear-gradient(90deg,#050505,#3a3a3a 70%,#0b0b0b)"><span class="badge"></span></div><h4>Sonatas Pathetique, Aurora, Appassionata</h4><p>Appassionata" means "passionate," and Velharo stuck to that. He relied entirely on expression. He shaped the first movement with utmost expressiveness and intensity.</p><a>Learn More →</a></div>
<div class="press-item abs" style="left:460px;top:2902px"><div class="cover" role="img" aria-label="CD cover: edition vol. 8, preludes and variations" style="background:linear-gradient(90deg,#3c5a40,#a8b48a 55%,#d8cfa2)"><span class="badge"></span></div><h4>Skarovin, Ravenkov, Prolanov</h4><p>Appassionata" means "passionate," and Velharo stuck to that. He relied entirely on expression. He shaped the first movement with utmost expressiveness and intensity.</p><a>Learn More →</a></div>
<div class="press-item abs" style="left:760px;top:2902px"><div class="cover" role="img" aria-label="CD cover: edition vol. 4, etudes" style="background:linear-gradient(90deg,#e8dcc8,#8a6a56 45%,#e4d6bc)"><span class="badge"></span></div><h4>Frederic Calvany Edition Vol. 10 – Mazurkas</h4><p>Appassionata" means "passionate," and Velharo stuck to that. He relied entirely on expression. He shaped the first movement with utmost expressiveness and intensity.</p><a>Learn More →</a></div>
<div class="btn abs" style="left:520px;top:3387px;width:160px;height:33px">View All Press</div>

<div class="abs" style="left:0;top:3483px;width:1200px;height:620px;background:var(--teal-light)"></div>
<h2 class="section-h abs" style="top:3522px">VIDEOS</h2>
<div class="video abs" role="img" aria-label="Concert video still" style="left:176px;top:3602px;background:linear-gradient(135deg,#1a120a,#8a6a3a,#221812)"></div>
<div class="video abs" role="img" aria-label="Concert video still" style="left:389px;top:3602px;background:linear-gradient(135deg,#2a2018,#b89a74,#3a2a1e)"></div>
<div class="video abs" role="img" aria-label="Concert video still" style="left:603px;top:3602px;background:linear-gradient(135deg,#0a0a0a,#5a5a5a,#111)"></div>
<div class="video abs" role="img" aria-label="Concert video still" style="left:816px;top:3602px;background:linear-gradient(135deg,#151515,#6a6a60,#222)"></div>
<div class="video abs" role="img" aria-label="Concert video still" style="left:176px;top:3725px;background:linear-gradient(135deg,#0f0d0a,#6a5a40,#151210)"></div>
<div class="video abs" role="img" aria-label="Concert video still" style="left:389px;top:3725px;background:linear-gradient(135deg,#0c0c0c,#6a5e4a,#121212)"></div>
<div class="video abs" role="img" aria-label="Concert hall video still" style="left:603px;top:3725px;background:linear-gradient(135deg,#3a2410,#c89a50,#2a1a0c)"></div>
<div class="video abs" role="img" aria-label="Concert video still" style="left:816px;top:3725px;background:linear-gradient(135deg,#0a0a0a,#4a4030,#111)"></div>
<div class="video abs" role="img" aria-label="Concert video still" style="left:176px;top:3849px;background:linear-gradient(135deg,#2a1a0c,#a07a48,#1a120a)"></div>
<div class="video abs" role="img" aria-label="Concert video still" style="left:389px;top:3849px;background:linear-gradient(135deg,#2a1e10,#b08656,#1a140c)"></div>
<div class="video abs" role="img" aria-label="Orchestra video still" style="left:603px;top:3849px;background:linear-gradient(135deg,#222,#8a7a6a,#333)"></div>
<div class="video abs" role="img" aria-label="Orchestra video still" style="left:816px;top:3849px;background:linear-gradient(135deg,#1c1c1c,#7a6a5a,#2c2c2c)"></div>

<div class="abs" style="left:0;top:4010px;width:1200px;height:484px;background:var(--black);clip-path:polygon(0 0,100% 16%,100% 100%,0 100%)"></div>
<div class="btn abs" style="left:520px;top:4003px;width:160px;height:33px;border:1px solid #fff">View All Videos</div>

<div class="brand abs" style="left:0;width:1200px;top:4222px;font-size:26px;text-align:center"><small style="font-size:10px">Tobias</small>VELHARO</div>
<div class="foot-nav abs"><span style="left:293px">Home</span><span style="left:412px">Biography</span><span style="left:549px">Repertoire</span><span style="left:671px">Press</span><span style="left:780px">Media</span><span style="left:898px">Contact</span></div>
<div class="abs" style="left:160px;top:4375px;width:880px;height:1px;background:#333"></div>
<div class="contact abs" style="left:294px"><span class="ico"><svg width="12" height="12" viewBox="0 0 24 24"><path d="M6 2l4 4-2 3c1 3 4 6 7 7l3-2 4 4-3 4C10 21 3 14 2 5z" fill="#fff"/></svg></span>+1 555 014 2290</div>
<div class="contact abs" style="left:502px"><span class="ico"><svg width="12" height="12" viewBox="0 0 24 24"><rect x="2" y="5" width="20" height="14" rx="2" fill="none" stroke="#fff" stroke-width="2"/><path d="M2 6l10 7 10-7" fill="none" stroke="#fff" stroke-width="2"/></svg></span>tobias@velharo.com</div>
<div class="contact abs" style="left:746px"><span class="ico"><svg width="12" height="12" viewBox="0 0 24 24"><path d="M12 2a7 7 0 0 0-7 7c0 5 7 13 7 13s7-8 7-13a7 7 0 0 0-7-7z" fill="#fff"/><circle cx="12" cy="9" r="2.5" fill="#4fb3c9"/></svg></span>122, Lorem ipsum dolrd</div>
<div class="abs" style="left:551px;top:4454px;display:flex;gap:30px"><span class="dotsoc"></span><span class="dotsoc"></span><span class="dotsoc"></span></div>

</body>
</html>
```